Business Card Design Project

We're looking for a unique business card design that stands out from the rest, using the brand and logo we've already developed.
Two-sided design please.
Vantor Creative (www.vantorcreative.example.au) is a digitally-focused advertising agency that has produces results-driven campaigns. As a result, we'd like our business card to reflect our innovative approach.
Size, shape, orientation, etc, are all flexible (providing the print costs don't become ridiculous or we have to sit there with tiny scissors!).
Business card should include space for name, title, email, mobile, landline and address.

```html
<!DOCTYPE html>
<html lang="en">
<head>
<meta charset="utf-8">
<title>Vantor Creative — Business Card</title>
<link rel="stylesheet" href="https://fonts.googleapis.com/css2?family=Josefin+Sans:wght@400;600&family=Bebas+Neue&family=Open+Sans:wght@400;600&display=swap">
<style>
  :root {
    --stage: #e9e7e4;
    --orange: #f07a24;
    --orange-deep: #e2601a;
    --ink: #2a2a2a;
    --paper: #fbfbfb;
    --band: #f2f2f2;
    --rule: #3a3a3a;
  }
  * { margin: 0; padding: 0; box-sizing: border-box; }
  html, body {
    width: 1200px; height: 900px; overflow: hidden;
    background: var(--stage);
    font-family: "Open Sans", sans-serif;
    color: var(--ink);
  }
  .card {
    position: absolute;
    width: 560px; height: 320px;
    border-radius: 4px;
    overflow: hidden;
    box-shadow: 0 10px 28px rgba(0,0,0,.18);
  }
  /* Front side */
  .card-front {
    left: 60px; top: 90px;
    background: linear-gradient(135deg, var(--orange-deep), var(--orange) 70%);
  }
  .card-front .pattern-area {
    position: absolute; inset: 0 0 40px 0;
    background: linear-gradient(160deg, rgba(0,0,0,.06), rgba(255,255,255,.05));
  }
  .card-front .base-band {
    position: absolute; left: 0; right: 0; bottom: 0; height: 40px;
    background: var(--band);
  }
  .front-wordmark {
    position: absolute; left: 0; right: 0; top: 118px;
    text-align: center;
    font-family: "Josefin Sans", sans-serif;
    font-weight: 400;
    font-size: 46px; letter-spacing: 2px;
    color: var(--ink);
  }
  /* Back side */
  .card-back {
    left: 580px; top: 490px;
    background: var(--paper);
  }
  .card-back .base-band {
    position: absolute; left: 0; right: 0; bottom: 0; height: 26px;
    background: var(--ink);
  }
  .back-wordmark {
    position: absolute; left: 34px; top: 96px;
    width: 210px;
    font-family: "Josefin Sans", sans-serif;
    font-weight: 400;
    font-size: 28px; line-height: 1.1; letter-spacing: 1px;
    color: var(--ink);
  }
  .divider {
    position: absolute; left: 258px; top: 70px;
    width: 2px; height: 110px; background: var(--rule);
  }
  .details { position: absolute; left: 276px; top: 76px; right: 18px; }
  .name-line { display: flex; align-items: baseline; gap: 8px; }
  .person-name {
    font-family: "Bebas Neue", sans-serif;
    font-size: 32px; letter-spacing: 1px; color: var(--ink);
  }
  .person-title {
    font-size: 10.5px; color: #555;
    border-left: 2px solid var(--orange); padding-left: 6px;
  }
  .contacts {
    display: grid; grid-template-columns: 1fr 1.35fr;
    gap: 5px 10px; margin-top: 8px;
    font-size: 10px; font-weight: 600; color: var(--ink);
  }
  .contact { display: flex; align-items: center; gap: 6px; white-space: nowrap; }
  .contact svg { width: 11px; height: 11px; flex: none; fill: var(--orange); }
  .address { grid-column: 1 / -1; font-size: 10px; font-weight: 600; margin-top: 3px; }
</style>
</head>
<body>
  <section class="card card-front" aria-label="Card front">
    <div class="pattern-area" role="img" aria-label="Faint repeating brand pattern on orange"></div>
    <div class="front-wordmark">Vantor Creative</div>
    <div class="base-band"></div>
  </section>

  <section class="card card-back" aria-label="Card back">
    <div class="back-wordmark">Vantor Creative</div>
    <div class="divider"></div>
    <div class="details">
      <div class="name-line">
        <h1 class="person-name">Marek Ellison</h1>
        <span class="person-title">Managing Director</span>
      </div>
      <div class="contacts">
        <div class="contact">
          <svg viewBox="0 0 12 12"><rect x="1" y="1" width="10" height="10" rx="1.5"/><rect x="3" y="3" width="6" height="3" fill="#fff"/></svg>
          +1 555 01 23
        </div>
        <div class="contact">
          <svg viewBox="0 0 12 12"><circle cx="6" cy="6" r="5"/><path d="M1 6h10M6 1c2 2 2 8 0 10M6 1c-2 2-2 8 0 10" stroke="#fff" stroke-width=".8" fill="none"/></svg>
          www.vantorcreative.example.au
        </div>
        <div class="contact">
          <svg viewBox="0 0 12 12"><rect x="3" y="0.5" width="6" height="11" rx="1.2"/><rect x="4" y="2" width="4" height="6.5" fill="#fff"/></svg>
          +1 555 01 89
        </div>
        <div class="contact">
          <svg viewBox="0 0 12 12"><rect x="0.5" y="2.5" width="11" height="7" rx="1"/><path d="M1 3l5 4 5-4" stroke="#fff" stroke-width="1" fill="none"/></svg>
          info@vantorcreative.example.au
        </div>
        <div class="address">N14 Harlow Street, Elmsworth, Mauritius</div>
      </div>
    </div>
    <div class="base-band"></div>
  </section>
</body>
</html>
```